Barrowdale Groundworks Business Card Design

We are a new company base in Far North Queensland Australia called Barrowdale Groundworks. We are a company that hire machinery (graders, rollers, excavators and trucks) for road construction and earthworks. We also supply quarry products to the building and construction industries. (Crushed aggregates, road base materials, sand, gravel and rocks). Would like a logo that can also be used on our plant to advertise us.
Target Market(s)
engineers, builders and general public
Industry/Entity Type
Construction
Contact Information for Business Card
Barrowdale Groundworks Pty Ltd, Dennis and Maureen Holt
ABN: 58 302 719 046 ACN: 302 719 046
PO Box 17, Cooktown Qld 4895
Pardoe Street Cooktown Qld 4895

```html
<!DOCTYPE html>
<html lang="en">
<head>
<meta charset="utf-8">
<title>Barrowdale Groundworks – Business Card</title>
<link rel="stylesheet" href="https://fonts.googleapis.com/css2?family=Tulpen+One&display=swap">
<style>
  :root {
    --card-bg: #4a4a4a;
    --title-ink: #1e1e1e;
    --details-ink: #ffffff;
    --phone-ink: #2a2a2a;
  }
  * { margin: 0; padding: 0; box-sizing: border-box; }
  html, body {
    width: 1200px;
    height: 741px;
    overflow: hidden;
    background: var(--card-bg);
  }
  .card {
    position: relative;
    width: 1200px;
    height: 741px;
    background: var(--card-bg);
    font-family: "Tulpen One", "Arial Narrow", sans-serif;
    text-align: center;
  }
  .brand-name {
    position: absolute;
    left: 0;
    right: 0;
    top: 116px;
    font-size: 148px;
    line-height: 1;
    font-weight: 400;
    color: var(--title-ink);
    letter-spacing: 0;
  }
  .company-details {
    position: absolute;
    left: 60px;
    right: 60px;
    top: 350px;
    font-size: 42px;
    line-height: 48px;
    color: var(--details-ink);
  }
  .phone-list {
    position: absolute;
    left: 0;
    right: 0;
    top: 519px;
    list-style: none;
    font-size: 42px;
    line-height: 49px;
    color: var(--phone-ink);
  }
</style>
</head>
<body>
  <main class="card">
    <h1 class="brand-name">Barrowdale Groundworks</h1>
    <p class="company-details">
      Barrowdale Groundworks Pty Ltd, Dennis and Maureen Holt ABN: 58 302 719 046 ACN: 302 719 046 PO Box 17,<br>
      Kelverton Qld 4871 Pardoe Street Kelverton Qld 4871
    </p>
    <ul class="phone-list">
      <li class="phone-mobile">Mobile: 04 27 518 304</li>
      <li class="phone-office">Office Ph / Fax: 07 40 612 359</li>
    </ul>
  </main>
</body>
</html>
```